Business Card Design needed - Something Awesome!

Need a business card designed. Company is "Harbor Vane Consulting" we do consulting and also have sales automation technology.
I'm going to use thick stock or metal, something really nice... I was thinking about a QR Code on the back that would just upload my contact info to the persons contact, etc -

This is a Strategy Company with a tech feel. I'm open to ideas but really want this to be nice!

I need a template that should include:

Name | Position or Title
D: 555.203.8146
www.harborvaneconsulting.example

I'm going to attach my contact so you can use that one, I need to get this printed.

Target Market(s)

Small to mid size customers, Entrepreneurs etc.

Industry/Entity Type

Consulting, Tech, Private Equity.

Contact Information for Business Card

Name, Phone, Maybe email, URL

Font styles to use
Sans Serif

Colors

Designer to choose only greyscale colors for use in the design.

Requirements
Must have
• Fresh, Clean, stand out from the crowd - will be on thick stock or metal.
Nice to have
• Clean, simple yet impactful.
Should not have
• Not cartoonish

```html
<!DOCTYPE html>
<html lang="en">
<head>
<meta charset="utf-8">
<title>Harbor Vane Consulting — Business Card</title>
<link rel="stylesheet" href="https://fonts.googleapis.com/css2?family=Oxygen:wght@400;700&display=swap">
<style>
  :root {
    --page: #fdfdfd;
    --card-light: #f4f4f4;
    --card-dark: #040404;
    --ink: #1a1a1a;
    --ink-soft: #505050;
    --mark-grey: #999999;
    --strip-light: #9a9a9a;
    --strip-mid: #747474;
    --strip-deep: #3a3a3a;
  }
  * { margin: 0; padding: 0; box-sizing: border-box; }
  html, body {
    width: 1200px;
    height: 1200px;
    overflow: hidden;
    background: var(--page);
    font-family: "Oxygen", sans-serif;
  }
  .card {
    position: absolute;
    left: 319px;
    width: 569px;
    height: 356px;
    overflow: hidden;
  }
  .card--front { top: 233px; background: var(--card-light); }
  .card--back  { top: 617px; background: var(--card-dark); }

  .pattern-strip {
    position: absolute;
    top: 0;
    right: 0;
    width: 123px;
    height: 100%;
    background: linear-gradient(90deg, var(--strip-light) 0%, var(--strip-mid) 50%, var(--strip-deep) 100%);
  }

  .brand-vertical {
    position: absolute;
    left: 408px;
    top: 411px;
    transform: translate(-50%, -50%) rotate(-90deg);
    white-space: nowrap;
    font-size: 30px;
    font-weight: 700;
    letter-spacing: 2px;
    color: var(--ink);
  }

  .contact {
    position: absolute;
    left: 142px;
    top: 197px;
    color: var(--ink);
  }
  .contact__name {
    font-size: 22px;
    font-weight: 400;
    line-height: 26px;
  }
  .contact__title {
    font-size: 18px;
    line-height: 24px;
    color: var(--ink-soft);
  }
  .contact__phone {
    margin-top: 10px;
    font-size: 19px;
    line-height: 24px;
  }
  .contact__web {
    margin-top: 3px;
    font-size: 15.5px;
    line-height: 22px;
    color: var(--ink-soft);
    letter-spacing: 0.3px;
  }

  .brand-centre {
    position: absolute;
    left: 232px;
    top: 178px;
    transform: translate(-50%, -50%);
    white-space: nowrap;
    font-size: 28px;
    font-weight: 700;
    letter-spacing: 2px;
    color: var(--mark-grey);
  }
</style>
</head>
<body>
  <section class="card card--front">
    <div class="brand-vertical" style="left:89px; top:178px;">HARBOR VANE</div>
    <div class="contact">
      <p class="contact__name">Dorian K. Ashford</p>
      <p class="contact__title">Founder / CEO</p>
      <p class="contact__phone">D: 555.203.8146</p>
      <p class="contact__web">www.harborvaneconsulting.example</p>
    </div>
    <div class="pattern-strip" role="img" aria-label="Greyscale diamond tile pattern running down the right edge"></div>
  </section>

  <section class="card card--back">
    <div class="brand-centre">HARBOR VANE</div>
    <div class="pattern-strip" role="img" aria-label="Greyscale diamond tile pattern running down the right edge"></div>
  </section>
</body>
</html>
```